BRIGHTWELL PROPERTY CHECKS Business card, please make it match the flyer.
Dana Kowalt
Dana@brightwellpropertychecksfl.example
352-555-0187 office
www.BrightwellPropertyChecks.example

Contact Information for Business Card

OUR LOGO

```html
<!DOCTYPE html>
<html lang="en">
<head>
<meta charset="utf-8">
<title>Brightwell Property Checks – Business Card</title>
<link href="https://fonts.googleapis.com/css2?family=Montserrat:wght@500;600;800&family=Oswald:wght@700&display=swap" rel="stylesheet">
<style>
  :root {
    --page: #c9c9c9;
    --card-black: #161616;
    --card-dark: #222222;
    --flag-navy: #1e2a44;
    --flag-red: #4a1518;
    --paper: #ffffff;
    --accent-yellow: #f6ea12;
    --ink-navy: #1b3263;
    --signal-red: #e41d24;
  }
  * { box-sizing: border-box; margin: 0; padding: 0; }
  html, body { width: 1200px; height: 800px; overflow: hidden; }
  body {
    background: var(--page);
    display: flex;
    flex-direction: column;
    align-items: center;
    justify-content: center;
    gap: 30px;
    font-family: "Montserrat", sans-serif;
  }
  .card {
    position: relative;
    width: 620px;
    height: 354px;
    border-radius: 18px;
    overflow: hidden;
    background: var(--card-black);
    box-shadow: 0 10px 24px rgba(0,0,0,0.25);
  }
  .card-texture {
    position: absolute;
    inset: 0;
    background:
      radial-gradient(ellipse at 75% 20%, var(--flag-red) 0%, transparent 45%),
      radial-gradient(ellipse at 40% 70%, var(--flag-navy) 0%, transparent 50%),
      linear-gradient(135deg, var(--card-black) 0%, var(--card-dark) 55%, var(--card-black) 100%);
    opacity: 0.85;
  }
  .contact-band {
    position: absolute;
    inset: 0;
    width: 100%;
    height: 100%;
  }
  .holder-name {
    position: absolute;
    left: 150px;
    top: 96px;
    font-family: "Oswald", sans-serif;
    font-weight: 700;
    font-size: 58px;
    line-height: 1;
    letter-spacing: -0.5px;
    color: var(--paper);
    text-transform: uppercase;
  }
  .holder-name .first { color: var(--accent-yellow); }
  .call-tag {
    position: absolute;
    left: 262px;
    top: 176px;
    width: 176px;
    height: 42px;
  }
  .call-tag-label {
    position: absolute;
    left: 290px;
    top: 185px;
    font-weight: 600;
    font-size: 20px;
    letter-spacing: 1px;
    color: var(--ink-navy);
  }
  .phone-row {
    position: absolute;
    left: 196px;
    top: 226px;
    display: flex;
    align-items: center;
    gap: 12px;
  }
  .phone-icon { width: 38px; height: 38px; }
  .phone-number {
    font-weight: 800;
    font-size: 36px;
    letter-spacing: 0.5px;
    color: var(--ink-navy);
  }
  .contact-lines {
    position: absolute;
    left: 198px;
    top: 278px;
    font-weight: 500;
    font-size: 16px;
    line-height: 25px;
    color: var(--ink-navy);
  }
  .back-brand {
    position: absolute;
    inset: 0;
    display: flex;
    align-items: center;
    justify-content: center;
    gap: 16px;
  }
  .brand-dot {
    width: 34px;
    height: 34px;
    border-radius: 50%;
    background: var(--signal-red);
  }
  .brand-name {
    font-family: "Oswald", sans-serif;
    font-weight: 700;
    font-size: 34px;
    color: var(--paper);
    letter-spacing: 1px;
  }
</style>
</head>
<body>
  <section class="card card-front">
    <div class="card-texture" role="img" aria-label="Dark brushed metal and flag texture background"></div>
    <svg class="contact-band" viewBox="0 0 620 354" aria-hidden="true">
      <polygon points="0,236 620,166 620,354 0,354" fill="var(--paper)"/>
      <line x1="0" y1="236" x2="620" y2="166" stroke="var(--accent-yellow)" stroke-width="6"/>
    </svg>
    <h1 class="holder-name"><span class="first">Dana</span> Kowalt</h1>
    <svg class="call-tag" viewBox="0 0 176 42" aria-hidden="true">
      <polygon points="10,0 176,0 168,42 0,42" fill="var(--accent-yellow)"/>
    </svg>
    <span class="call-tag-label">CALL NOW</span>
    <div class="phone-row">
      <svg class="phone-icon" viewBox="0 0 38 38" aria-hidden="true">
        <circle cx="19" cy="19" r="19" fill="var(--signal-red)"/>
        <path d="M11 20c0-5 3.5-8 8-8s8 3 8 8l-3 1-1-3c-2-1-6-1-8 0l-1 3z" fill="var(--paper)"/>
        <rect x="14" y="22" width="10" height="5" rx="1.5" fill="var(--paper)"/>
      </svg>
      <span class="phone-number">352-555-0187</span>
    </div>
    <div class="contact-lines">
      <div class="contact-email">Dana@brightwellpropertychecksfl.example</div>
      <div class="contact-web">www.BrightwellPropertyChecks.example</div>
    </div>
  </section>

  <section class="card card-back">
    <div class="card-texture" role="img" aria-label="Dark brushed metal and flag texture background"></div>
    <div class="back-brand">
      <span class="brand-dot"></span>
      <span class="brand-name">BRIGHTWELL PROPERTY CHECKS</span>
    </div>
  </section>
</body>
</html>
```